Brightpath Dental Studio

Please go to www.brightpathdentalstudio.example and obtain the current company logo.
Doctors name are
Marita Velbonne, DDS
Denis Kalb, DMD
Addresses are
318 Larchmont Ave
Larkfield, NJ 07012
201-555-0147
And
872 14th St.
North Bayview, NJ 07021
201-555-0182
Theme of the business card should feel modrrn and similar to the website.
Front side should include company logo, doctors name, addresses, phone numbers.
Back of the card should include blank lines for patient's name. Date and time for next scheduled appointment. And notice of 24-hr cancellation courtesy policy.
Dental

```html
<!DOCTYPE html>
<html lang="en">
<head>
<meta charset="utf-8">
<title>Brightpath Dental Studio – Business Card</title>
<link href="https://fonts.googleapis.com/css2?family=Source+Sans+3:ital,wght@0,400;0,600;1,400&display=swap" rel="stylesheet">
<style>
  :root {
    --backdrop: #5b4a3c;
    --card: #ffffff;
    --navy: #232a5c;
    --ink: #4a4a4a;
    --rule: #9a9a9a;
    --dots: #8a8a8a;
  }
  * { box-sizing: border-box; margin: 0; padding: 0; }
  html, body { width: 1200px; height: 987px; overflow: hidden; }
  body {
    background: var(--backdrop);
    font-family: "Source Sans 3", "Myriad Pro", Arial, sans-serif;
    position: relative;
  }
  .card {
    position: absolute;
    left: 293px;
    width: 615px;
    height: 352px;
    background: var(--card);
    border-radius: 20px;
    box-shadow: 0 3px 8px rgba(0,0,0,0.35);
  }
  .card--front { top: 130px; }
  .card--back { top: 505px; }

  /* Front */
  .brand-name {
    position: absolute;
    top: 68px; left: 0; right: 0;
    text-align: center;
    color: var(--navy);
    font-weight: 600;
    font-size: 34px;
    letter-spacing: 0.5px;
  }
  .doctors {
    position: absolute;
    top: 176px; left: 0; right: 0;
    text-align: center;
    color: var(--navy);
    font-weight: 600;
    font-size: 22px;
    line-height: 31px;
  }
  .divider {
    position: absolute;
    top: 244px; left: 39px; right: 39px;
    border-top: 1px solid var(--rule);
  }
  .office {
    position: absolute;
    top: 254px;
    color: var(--ink);
    font-size: 16px;
    font-style: normal;
    line-height: 22px;
  }
  .office--left { left: 39px; }
  .office--right { right: 39px; text-align: right; }
  .phone { display: flex; align-items: center; gap: 8px; }
  .office--right .phone { justify-content: flex-end; }
  .phone svg { width: 14px; height: 14px; fill: var(--navy); }

  /* Back */
  .appt-title {
    position: absolute;
    top: 26px; left: 0; right: 0;
    text-align: center;
    color: var(--navy);
    font-weight: 600;
    font-size: 23px;
  }
  .field {
    position: absolute;
    display: flex;
    align-items: flex-end;
    color: var(--navy);
    font-size: 17px;
  }
  .field .fill {
    flex: 1;
    border-bottom: 1.5px dotted var(--dots);
    margin-left: 12px;
    margin-bottom: 5px;
  }
  .field .suffix { font-size: 13px; margin-left: 6px; margin-bottom: 1px; }
  .field--name { top: 84px; left: 40px; right: 40px; }
  .field--date { top: 140px; left: 40px; width: 292px; }
  .field--time { top: 140px; left: 351px; right: 40px; }
  .field--note { top: 192px; left: 40px; right: 44px; }
  .blank-line {
    position: absolute;
    left: 40px; right: 44px;
    border-bottom: 1.5px dotted var(--dots);
  }
  .blank-line--one { top: 238px; }
  .blank-line--two { top: 272px; }
  .policy {
    position: absolute;
    top: 292px; left: 0; right: 0;
    text-align: center;
    color: var(--ink);
    font-style: italic;
    font-size: 13px;
    line-height: 19px;
  }
</style>
</head>
<body>
  <section class="card card--front">
    <div class="brand-name">Brightpath Dental Studio</div>
    <div class="doctors">
      <p>Marita Velbonne, DDS</p>
      <p>Denis Kalb, DMD</p>
    </div>
    <div class="divider"></div>
    <address class="office office--left">
      <p>318 Larchmont Ave</p>
      <p>Larkfield, NJ 07012</p>
      <p class="phone">
        <svg viewBox="0 0 24 24" aria-hidden="true"><path d="M6.6 10.8a15.1 15.1 0 0 0 6.6 6.6l2.2-2.2c.3-.3.7-.4 1-.2 1.1.4 2.3.6 3.6.6.6 0 1 .4 1 1V20c0 .6-.4 1-1 1A17 17 0 0 1 3 4c0-.6.4-1 1-1h3.5c.6 0 1 .4 1 1 0 1.3.2 2.5.6 3.6.1.3 0 .7-.2 1z"/></svg>
        201-555-0147
      </p>
    </address>
    <address class="office office--right">
      <p>872 14th St.</p>
      <p>North Bayview, NJ 07021</p>
      <p class="phone">
        201-555-0182
        <svg viewBox="0 0 24 24" aria-hidden="true"><path d="M6.6 10.8a15.1 15.1 0 0 0 6.6 6.6l2.2-2.2c.3-.3.7-.4 1-.2 1.1.4 2.3.6 3.6.6.6 0 1 .4 1 1V20c0 .6-.4 1-1 1A17 17 0 0 1 3 4c0-.6.4-1 1-1h3.5c.6 0 1 .4 1 1 0 1.3.2 2.5.6 3.6.1.3 0 .7-.2 1z"/></svg>
      </p>
    </address>
  </section>

  <section class="card card--back">
    <h2 class="appt-title">Next Appointment</h2>
    <div class="field field--name"><span>Name :</span><span class="fill"></span></div>
    <div class="field field--date"><span>Date :</span><span class="fill"></span></div>
    <div class="field field--time"><span>Time :</span><span class="fill"></span><span class="suffix">AM/PM</span></div>
    <div class="field field--note"><span>Note :</span><span class="fill"></span></div>
    <div class="blank-line blank-line--one"></div>
    <div class="blank-line blank-line--two"></div>
    <p class="policy">Please give me 24 hours notice if you are unable to keep your appointment or<br>a cancellation fee may be charged.</p>
  </section>
</body>
</html>
```